Consulting Company PowerPoint Template Design

We are looking for an updated PowerPoint template design or our 55 person energy consulting firm (K7) based in San Francisco (www.kayseven.example). We would like two versions of the same PowerPoint template in a 16:9 and 4:3 format with our existing logo.

We have an existing color scheme and template and are seeking your help to polish/update the template design for wide format and create a flexible template that is easy to use with content from Excel and Word. Our current template, and a couple of examples that we like are attached.

Specific requests include:

• Dark background for slide title
• A narrow section header
• Maximizing white space for content
• A limited number of well designed Master template layouts to choose from
• A selection of title and section header slides that are not San Francisco specific with some variety to chose from ideally with a focus on energy or nature, graphics/visuals.

For examples of energy specific templates see:
https://www.brightslidery.example/energy/powerpoint-templates/0.html

Requirements
Must have
• Must use our logo but open to other designs, fonts, and styles for the PowerPoint template.
• Please use our existing color scheme found in the attached Excel file.
• Also we would like the ability to easily copy and paste from our existing/original template to the new template. In other words we would like backward compatibility to apply the new template format to our old PowerPoints that use our existing template.

```html
<!DOCTYPE html>
<html lang="en">
<head>
<meta charset="utf-8">
<title>K7 Presentation Template Overview</title>
<link href="https://fonts.googleapis.com/css2?family=Roboto:wght@300;400;500;700&family=Roboto+Condensed:wght@400;700&display=swap" rel="stylesheet">
<style>
:root{
  --canvas:#d8d8da;
  --teal:#1b5b79;
  --teal-dark:#124b66;
  --teal-deep:#0f3f56;
  --gold:#c9a867;
  --gold-soft:#d9bd83;
  --grey:#8c8c8e;
  --ink:#3a3a3a;
  --paper:#ffffff;
}
*{margin:0;padding:0;box-sizing:border-box}
html,body{width:1200px;height:900px;overflow:hidden;background:var(--canvas);font-family:"Roboto",Arial,sans-serif;color:var(--ink)}
.board{position:relative;width:1200px;height:900px}
.slide{position:absolute;width:266px;height:150px;background:var(--paper);overflow:hidden}
.c1{left:202px}.c2{left:472px}.c3{left:742px}
.r1{top:77px}.r2{top:233px}.r3{top:392px}.r4{top:549px}.r5{top:706px}
.abs{position:absolute}
.heading{position:absolute;top:11px;left:10px;font-family:"Roboto Condensed",sans-serif;font-size:7.5px;color:var(--teal);letter-spacing:.1px}
.heading b{font-weight:400;border-bottom:1px solid var(--gold);padding-bottom:1px}
.footer-mark{position:absolute;left:7px;bottom:4px;width:6px;height:6px;background:var(--teal)}
.footer-name{position:absolute;right:6px;bottom:5px;font-size:2.8px;color:var(--teal);font-weight:500}
.wordmark{position:absolute;font-size:4px;font-weight:500;color:var(--teal)}
.wordmark-box{position:absolute;width:9px;height:9px;background:var(--teal)}
.body{font-size:2.9px;line-height:4.1px;color:#555;text-align:justify}
.title-sm{font-size:5.6px;color:var(--teal);font-weight:500}
.photo{position:absolute}
.icon-ring{position:absolute;width:14px;height:14px;border-radius:50%;border:1px solid #c9d7df;display:flex;align-items:center;justify-content:center}
.icon-ring svg{width:7px;height:7px}
.cap{font-size:2.8px;line-height:3.8px;color:#555;text-align:center}
.gold-dot{position:absolute;width:9px;height:9px;border-radius:50%;background:var(--gold);color:#fff;font-size:4px;display:flex;align-items:center;justify-content:center}
.toc-item{position:absolute;font-size:3.3px;line-height:4.2px;color:#fff;font-weight:700}
.tile-text{position:absolute;font-size:2.9px;line-height:3.9px;color:#fff;font-weight:700;padding:5px}
</style>
</head>
<body>
<main class="board">

<!-- 1 Welcome -->
<section class="slide c1 r1">
  <div class="photo" style="inset:0;background:linear-gradient(160deg,#3f6f88 0%,#24546e 45%,#123e56 100%)" role="img" aria-label="City skyline at dusk with teal overlay"></div>
  <div class="abs" style="right:23px;top:72px;font-family:'Roboto Condensed',sans-serif;font-size:12px;color:#fff">WELCOME</div>
  <div class="abs" style="right:23px;top:87px;font-size:6.5px;letter-spacing:1.3px;color:#fff">TO OUR PRESENTATION</div>
  <div class="abs" style="left:0;right:0;top:110px;height:20px;background:#fff"></div>
  <div class="wordmark-box" style="left:19px;top:115.5px"></div>
  <div class="wordmark" style="left:32px;top:117.5px">K7 Consulting</div>
</section>

<!-- 2 Contents -->
<section class="slide c2 r1">
  <div class="photo" style="inset:0;background:radial-gradient(circle at 55% 30%,#3a7486 0%,#1c5b72 40%,#155268 100%)" role="img" aria-label="Hands holding a globe over green grass with teal overlay"></div>
  <div class="abs" style="left:43px;top:42px;font-size:4px;color:#fff">TABLE OF</div>
  <div class="abs" style="left:43px;top:48px;font-family:'Roboto Condensed',sans-serif;font-size:9.5px;color:#fff;border-bottom:1px solid var(--gold)">CONTENTS</div>
  <div class="gold-dot" style="left:59px;top:78px">1</div><div class="toc-item" style="left:72px;top:78px">LOREM IPSUM DOLOR SIT<br>MET DOLOR SIT MET</div>
  <div class="gold-dot" style="left:59px;top:98px">1</div><div class="toc-item" style="left:72px;top:98px">LOREM IPSUM DOLOR SIT<br>MET DOLOR SIT MET</div>
  <div class="gold-dot" style="left:59px;top:118px">1</div><div class="toc-item" style="left:72px;top:118px">LOREM IPSUM DOLOR SIT<br>MET DOLOR SIT MET</div>
  <div class="gold-dot" style="left:153px;top:78px">1</div><div class="toc-item" style="left:166px;top:78px">LOREM IPSUM DOLOR SIT<br>MET DOLOR SIT MET</div>
  <div class="gold-dot" style="left:153px;top:98px">1</div><div class="toc-item" style="left:166px;top:98px">LOREM IPSUM DOLOR SIT<br>MET DOLOR SIT MET</div>
  <div class="gold-dot" style="left:153px;top:118px">1</div><div class="toc-item" style="left:166px;top:118px">LOREM IPSUM DOLOR SIT<br>MET DOLOR SIT MET</div>
</section>

<!-- 3 About us: band -->
<section class="slide c3 r1">
  <div class="heading"><b>ABOUT</b> US</div>
  <div class="abs" style="left:0;top:45px;width:87px;height:47px;background:var(--teal-dark)"></div>
  <div class="tile-text" style="left:11px;top:54px;padding:0;font-size:2.8px;line-height:4px">LOREM IPSUM DOLOR SIT AMET<br>CONSECTETUR ADIPISCING ELIT, SED<br>DO EIUSMOD TEMPOR INCIDIDUNT<br>UT LABORE ET DOLORE MAGNA</div>
  <div class="photo" style="left:87px;top:45px;right:0;height:47px;background:linear-gradient(180deg,#5d6f86 0%,#c98a55 55%,#f0a040 70%,#6b5a4a 100%)" role="img" aria-label="Wind turbines on a plain at sunset"></div>
  <div class="body abs" style="left:87px;top:101px;width:170px">Lorem ipsum dolor sit amet, consectetur adipiscing elit, sed do eiusmod tempor incididunt ut labore et dolore magna aliqua. Ut enim ad minim veniam, quis nostrud exercitation ullamco laboris nisi ut aliquip ex ea commodo consequat. Duis aute irure dolor in reprehenderit in voluptate velit esse cillum dolore eu fugiat nulla pariatur.</div>
  <div class="footer-mark"></div><div class="footer-name">K7 Consulting &nbsp;|&nbsp; 1</div>
</section>

<!-- 4 About us: two columns -->
<section class="slide c1 r2">
  <div class="heading"><b>ABOUT</b> US</div>
  <div class="photo" style="left:10px;top:37px;width:56px;height:36px;background:linear-gradient(135deg,#9fb6c8,#d9b060 60%,#7c8b97)" role="img" aria-label="Engineers in hard hats reviewing plans"></div>
  <div class="abs" style="left:10px;top:75px;width:56px;font-size:2.9px;line-height:3.9px;text-align:right;color:var(--teal);font-weight:500">Lorem ipsum dolor sit amet<br>consectetur adipiscing<br>elit sed do eiusmod</div>
  <div class="body abs" style="left:76px;top:37px;width:83px">Lorem ipsum dolor sit amet, consectetur adipiscing elit, sed do eiusmod tempor incididunt ut labore et dolore magna aliqua. Ut enim ad minim veniam, quis nostrud exercitation ullamco laboris nisi ut aliquip ex ea commodo consequat. Duis aute irure dolor in reprehenderit in voluptate velit esse cillum dolore eu fugiat nulla pariatur.<br><br>Lorem ipsum dolor sit amet, consectetur adipiscing elit, sed do eiusmod tempor incididunt ut labore et dolore magna aliqua. Ut enim ad minim veniam, quis nostrud exercitation ullamco laboris nisi ut aliquip ex ea commodo consequat. Duis aute irure dolor in reprehenderit in voluptate velit esse cillum dolore eu.</div>
  <div class="body abs" style="left:169px;top:37px;width:83px">Lorem ipsum dolor sit amet, consectetur adipiscing elit, sed do eiusmod tempor incididunt ut labore et dolore magna aliqua. Ut enim ad minim veniam, quis nostrud exercitation ullamco laboris nisi ut aliquip ex ea commodo consequat. Duis aute irure dolor in reprehenderit in voluptate velit esse cillum dolore eu fugiat nulla pariatur.<br><br>Lorem ipsum dolor sit amet, consectetur adipiscing elit, sed do eiusmod tempor incididunt ut labore et dolore magna aliqua. Ut enim ad minim veniam, quis nostrud exercitation ullamco laboris nisi ut aliquip ex ea commodo consequat. Duis aute irure dolor in reprehenderit in voluptate velit esse cillum dolore eu.</div>
  <div class="footer-mark"></div><div class="footer-name">K7 Consulting &nbsp;|&nbsp; 1</div>
</section>

<!-- 5 About us: teal panel with icons -->
<section class="slide c2 r2">
  <div class="photo" style="left:18px;top:0;width:108px;height:150px;background:linear-gradient(180deg,#2d6d88 0%,#1e5b76 60%,#2f6170 100%)" role="img" aria-label="Wind turbine over a field with teal overlay"></div>
  <div class="abs" style="left:27px;top:68px;font-size:5.6px;color:#fff">Lorem ipsum dolor sit amet</div>
  <div class="abs" style="left:27px;top:77px;width:92px;font-size:2.8px;line-height:3.9px;color:#fff;font-weight:700">Lorem ipsum dolor sit amet, consectetur adipiscing elit, sed do eiusmod tempor incididunt ut labore et dolore magna aliqua. Ut enim ad minim veniam, quis nostrud exercitation ullamco laboris nisi ut aliquip ex ea commodo consequat. Duis aute irure dolor in reprehenderit in voluptate velit esse cillum dolore eu fugiat nulla pariatur.</div>
  <div class="heading" style="left:138px"><b>ABOUT</b> US</div>
  <div class="icon-ring" style="left:151px;top:42px"><svg viewBox="0 0 10 10"><circle cx="4" cy="4" r="2.8" fill="none" stroke="#1b5b79" stroke-width="1.3"/><path d="M6 6l3 3" stroke="#1b5b79" stroke-width="1.5"/></svg></div>
  <div class="icon-ring" style="left:151px;top:73px"><svg viewBox="0 0 10 10"><path d="M1 9h8M2 8V5M4.5 8V2M7 8V4" stroke="#1b5b79" stroke-width="1.5"/></svg></div>
  <div class="icon-ring" style="left:151px;top:106px"><svg viewBox="0 0 10 10"><circle cx="5" cy="5.5" r="3.5" fill="none" stroke="#1b5b79" stroke-width="1.2"/><path d="M5 5.5V3.5M4 1h2" stroke="#1b5b79" stroke-width="1.2"/></svg></div>
  <div class="body abs" style="left:174px;top:42px;width:54px">Dolor sit amet, consectetur adipiscing elit, sed do eiusmod tempor</div>
  <div class="body abs" style="left:174px;top:73px;width:54px">Dolor sit amet, consectetur adipiscing elit, sed do eiusmod tempor</div>
  <div class="body abs" style="left:174px;top:106px;width:54px">Dolor sit amet, consectetur adipiscing elit, sed do eiusmod tempor</div>
  <div class="footer-mark"></div><div class="footer-name">K7 Consulting &nbsp;|&nbsp; 1</div>
</section>

<!-- 6 About us: gold panel -->
<section class="slide c3 r2">
  <div class="photo" style="left:14px;top:0;width:108px;height:150px;background:linear-gradient(160deg,#d8bc80,#c6a565 60%,#b99858)" role="img" aria-label="Engineers at a site with gold overlay"></div>
  <div class="abs" style="left:68px;top:30px;width:1px;height:90px;background:rgba(255,255,255,.6)"></div>
  <div class="abs" style="left:22px;top:75px;width:92px;height:1px;background:rgba(255,255,255,.6)"></div>
  <svg class="abs" style="left:37px;top:36px" width="9" height="9" viewBox="0 0 10 10"><path d="M5 1L9 5 5 9 1 5z" fill="#fff"/></svg>
  <svg class="abs" style="left:87px;top:36px" width="9" height="9" viewBox="0 0 10 10"><circle cx="4" cy="4" r="2.8" fill="none" stroke="#fff" stroke-width="1.3"/><path d="M6 6l3 3" stroke="#fff" stroke-width="1.5"/></svg>
  <svg class="abs" style="left:37px;top:81px" width="9" height="9" viewBox="0 0 10 10"><path d="M1 9h8M2 8V5M4.5 8V2M7 8V4" stroke="#fff" stroke-width="1.5"/></svg>
  <svg class="abs" style="left:87px;top:81px" width="9" height="9" viewBox="0 0 10 10"><circle cx="5" cy="5.5" r="3.5" fill="none" stroke="#fff" stroke-width="1.2"/><path d="M5 5.5V3.5" stroke="#fff" stroke-width="1.2"/></svg>
  <div class="cap abs" style="left:22px;top:50px;width:40px;color:#fff;font-weight:700">Dolor sit amet, consectetur adipiscing elit, sed do eiusmod tempor</div>
  <div class="cap abs" style="left:72px;top:50px;width:40px;color:#fff;font-weight:700">Dolor sit amet, consectetur adipiscing elit, sed do eiusmod tempor</div>
  <div class="cap abs" style="left:22px;top:95px;width:40px;color:#fff;font-weight:700">Dolor sit amet, consectetur adipiscing elit, sed do eiusmod tempor</div>
  <div class="cap abs" style="left:72px;top:95px;width:40px;color:#fff;font-weight:700">Dolor sit amet, consectetur adipiscing elit, sed do eiusmod tempor</div>
  <div class="heading" style="left:138px"><b>ABOUT</b> US</div>
  <div class="title-sm abs" style="left:141px;top:46px">Lorem ipsum dolor sit amet</div>
  <div class="body abs" style="left:141px;top:55px;width:114px">Lorem ipsum dolor sit amet, consectetur adipiscing elit, sed do eiusmod tempor incididunt ut labore et dolore magna aliqua. Ut enim ad minim veniam, quis nostrud exercitation ullamco laboris nisi ut aliquip ex ea commodo consequat. Duis aute irure dolor in reprehenderit in voluptate velit esse cillum dolore eu fugiat nulla pariatur.<br><br>Lorem ipsum dolor sit amet, consectetur adipiscing elit, sed do eiusmod tempor incididunt ut labore et dolore magna aliqua. Ut enim ad minim veniam, quis nostrud exercitation ullamco laboris nisi ut aliquip ex ea commodo consequat.</div>
  <div class="footer-mark"></div><div class="footer-name">K7 Consulting &nbsp;|&nbsp; 1</div>
</section>

<!-- 7 About us: text and three photos -->
<section class="slide c1 r3">
  <div class="heading"><b>ABOUT</b> US</div>
  <div class="title-sm abs" style="left:14px;top:42px">Lorem ipsum dolor sit amet</div>
  <div class="body abs" style="left:14px;top:51px;width:90px">Lorem ipsum dolor sit amet, consectetur adipiscing elit, sed do eiusmod tempor incididunt ut labore et dolore magna aliqua. Ut enim ad minim veniam, quis nostrud exercitation ullamco laboris nisi ut aliquip ex ea commodo consequat. Duis aute irure dolor in reprehenderit in voluptate velit esse cillum dolore eu fugiat nulla pariatur.<br><br>Lorem ipsum dolor sit amet, consectetur adipiscing elit, sed do eiusmod tempor incididunt ut labore et dolore magna aliqua. Ut enim ad minim veniam, quis nostrud.</div>
  <div class="photo" style="left:117px;top:37px;width:38px;height:46px;background:linear-gradient(180deg,#3a3560,#c77b2e 70%,#2b2a3a)" role="img" aria-label="City lights at night"></div>
  <div class="photo" style="left:164px;top:37px;width:38px;height:46px;background:linear-gradient(180deg,#6fa6cf,#a9c8de 60%,#3c6a88)" role="img" aria-label="Wind turbines under blue sky"></div>
  <div class="photo" style="left:211px;top:37px;width:38px;height:46px;background:linear-gradient(135deg,#b8c9d6,#d8b460 55%,#7e8c96)" role="img" aria-label="Engineers in hard hats on site"></div>
  <div class="body abs" style="left:117px;top:87px;width:38px">Duis aute irure dolor in reprehenderit in voluptate velit esse cillum dolore eu fugiat nulla pariatur.</div>
  <div class="body abs" style="left:164px;top:87px;width:38px">Duis aute irure dolor in reprehenderit in voluptate velit esse cillum dolore eu fugiat nulla pariatur.</div>
  <div class="body abs" style="left:211px;top:87px;width:38px">Duis aute irure dolor in reprehenderit in voluptate velit esse cillum dolore eu fugiat nulla pariatur.</div>
  <div class="footer-mark"></div><div class="footer-name">K7 Consulting &nbsp;|&nbsp; 1</div>
</section>

<!-- 8 About us: mosaic -->
<section class="slide c2 r3">
  <div class="heading"><b>ABOUT</b> US</div>
  <div class="photo" style="left:0;top:32px;width:67px;height:42px;background:linear-gradient(180deg,#8fb0cc,#e6ebee 55%,#4f7a3a)" role="img" aria-label="Modern building with solar roof"></div>
  <div class="abs" style="left:67px;top:32px;width:66px;height:58px;background:var(--gold)"></div>
  <div class="tile-text" style="left:67px;top:46px;width:66px">LOREM IPSUM DOLOR SIT MET CONSECTETUR ADIPISCING ELIT, SED DO EIUSMOD TEMPOR INC IDIDUNT UT LABORE ET</div>
  <div class="photo" style="left:133px;top:32px;width:67px;height:42px;background:linear-gradient(180deg,#c7d3dc,#7d8790 60%,#4a525a)" role="img" aria-label="Rows of solar panels"></div>
  <div class="abs" style="left:200px;top:32px;width:66px;height:58px;background:var(--gold)"></div>
  <div class="tile-text" style="left:200px;top:46px;width:66px">LOREM IPSUM DOLOR SIT MET CONSECTETUR ADIPISCING ELIT, SED DO EIUSMOD TEMPOR INC IDIDUNT UT LABORE ET</div>
  <div class="abs" style="left:0;top:74px;width:67px;height:60px;background:var(--teal-dark)"></div>
  <div class="tile-text" style="left:0;top:85px;width:67px">LOREM IPSUM DOLOR SIT MET CONSECTETUR ADIPISCING ELIT, SED DO EIUSMOD TEMPOR INC IDIDUNT UT LABORE ET</div>
  <div class="photo" style="left:67px;top:90px;width:66px;height:44px;background:linear-gradient(180deg,#e0702a,#f09a3a 55%,#3a2318)" role="img" aria-label="Wind turbines silhouetted at sunset"></div>
  <div class="abs" style="left:133px;top:74px;width:67px;height:60px;background:var(--teal-dark)"></div>
  <div class="tile-text" style="left:133px;top:85px;width:67px">LOREM IPSUM DOLOR SIT MET CONSECTETUR ADIPISCING ELIT, SED DO EIUSMOD TEMPOR INC IDIDUNT UT LABORE ET</div>
  <div class="photo" style="left:200px;top:90px;width:66px;height:44px;background:linear-gradient(160deg,#aab6bf,#4e5f6c 60%,#b0413a)" role="img" aria-label="Worker installing solar panels"></div>
  <div class="footer-mark"></div><div class="footer-name">K7 Consulting &nbsp;|&nbsp; 1</div>
</section>

<!-- 9 Wind photo with icons -->
<section class="slide c3 r3">
  <div class="photo" style="left:0;top:0;width:266px;height:80px;background:linear-gradient(180deg,#2f6f9e 0%,#8fb5cf 40%,#e6eef3 65%,#6f8ea3 100%)" role="img" aria-label="Wind turbines over snowy hills under a blue sky"></div>
  <div class="icon-ring" style="left:36px;top:89px"><svg viewBox="0 0 10 10"><circle cx="4" cy="4" r="2.8" fill="none" stroke="#1b5b79" stroke-width="1.3"/><path d="M6 6l3 3" stroke="#1b5b79" stroke-width="1.5"/></svg></div>
  <div class="icon-ring" style="left:100px;top:89px"><svg viewBox="0 0 10 10"><path d="M1 9h8M2 8V5M4.5 8V2M7 8V4" stroke="#1b5b79" stroke-width="1.5"/></svg></div>
  <div class="icon-ring" style="left:164px;top:89px"><svg viewBox="0 0 10 10"><circle cx="5" cy="5.5" r="3.5" fill="none" stroke="#1b5b79" stroke-width="1.2"/><path d="M5 5.5V3.5M4 1h2" stroke="#1b5b79" stroke-width="1.2"/></svg></div>
  <div class="icon-ring" style="left:223px;top:89px"><svg viewBox="0 0 10 10"><path d="M5 1L9 5 5 9 1 5z" fill="#1b5b79"/></svg></div>
  <div class="cap abs" style="left:16px;top:108px;width:54px">Dolor sit amet, consectetur adipiscing elit, sed do eiusmod tempor</div>
  <div class="cap abs" style="left:80px;top:108px;width:54px">Dolor sit amet, consectetur adipiscing elit, sed do eiusmod tempor</div>
  <div class="cap abs" style="left:144px;top:108px;width:54px">Dolor sit amet, consectetur adipiscing elit, sed do eiusmod tempor</div>
  <div class="cap abs" style="left:203px;top:108px;width:54px">Dolor sit amet, consectetur adipiscing elit, sed do eiusmod tempor</div>
  <div class="footer-mark"></div><div class="footer-name">K7 Consulting &nbsp;|&nbsp; 1</div>
</section>

<!-- 10 Our team -->
<section class="slide c1 r4">
  <div class="heading"><b>OUR</b> TEAM</div>
  <div class="photo" style="left:35px;top:45px;width:30px;height:30px;border-radius:50%;border:1.5px solid var(--teal);background:linear-gradient(180deg,#dfe3e6,#8a98a4)" role="img" aria-label="Portrait of team member"></div>
  <div class="photo" style="left:116px;top:45px;width:30px;height:30px;border-radius:50%;border:1.5px solid var(--teal);background:linear-gradient(180deg,#e8e2dc,#b4443c)" role="img" aria-label="Portrait of team member"></div>
  <div class="photo" style="left:199px;top:45px;width:30px;height:30px;border-radius:50%;border:1.5px solid var(--teal);background:linear-gradient(180deg,#e6e6e6,#5a5a5a)" role="img" aria-label="Portrait of team member"></div>
  <div class="abs" style="left:20px;top:79px;width:60px;text-align:center;font-size:3.3px;font-weight:700;color:var(--teal)">JONATHAN DOE<br><span style="font-weight:400;color:#666">President</span></div>
  <div class="abs" style="left:101px;top:79px;width:60px;text-align:center;font-size:3.3px;font-weight:700;color:var(--teal)">MELANIE DOE<br><span style="font-weight:400;color:#666">CEO / Founder</span></div>
  <div class="abs" style="left:184px;top:79px;width:60px;text-align:center;font-size:3.3px;font-weight:700;color:var(--teal)">NATALIE DOE<br><span style="font-weight:400;color:#666">Vice President</span></div>
  <div class="cap abs" style="left:20px;top:94px;width:60px">dolor sit amet, consectetur adipisicing elit, sed do eiusmod tempor incididunt ut labore et dolore magna aliqua. Ut enim ad minim veniam, quis nostrud exercitation ullamco laboris nisi ut fugiat nulla pariatur.</div>
  <div class="cap abs" style="left:101px;top:94px;width:60px">dolor sit amet, consectetur adipisicing elit, sed do eiusmod tempor incididunt ut labore et dolore magna aliqua. Ut enim ad minim veniam, quis nostrud exercitation ullamco laboris nisi ut fugiat nulla pariatur.</div>
  <div class="cap abs" style="left:184px;top:94px;width:60px">dolor sit amet, consectetur adipisicing elit, sed do eiusmod tempor incididunt ut labore et dolore magna aliqua. Ut enim ad minim veniam, quis nostrud exercitation ullamco laboris nisi ut fugiat nulla pariatur.</div>
  <div class="footer-mark"></div><div class="footer-name">K7 Consulting &nbsp;|&nbsp; 1</div>
</section>

<!-- 11 Infograph -->
<section class="slide c2 r4">
  <div class="heading"><b>INFO</b>GRAPH</div>
  <svg class="abs" style="left:90px;top:37px" width="88" height="88" viewBox="0 0 88 88">
    <g fill="none" stroke-width="15">
      <path d="M12 44 A32 32 0 0 1 44 12" stroke="#c9a867"/>
      <path d="M44 12 A32 32 0 0 1 76 44" stroke="#8c8c8e"/>
      <path d="M76 44 A32 32 0 0 1 44 76" stroke="#1b5b79"/>
      <path d="M44 76 A32 32 0 0 1 12 44" stroke="#8c8c8e"/>
    </g>
    <circle cx="56" cy="14" r="9" fill="#c9a867" stroke="#fff" stroke-width="1.5"/>
    <circle cx="74" cy="56" r="9" fill="#8c8c8e" stroke="#fff" stroke-width="1.5"/>
    <circle cx="32" cy="74" r="9" fill="#1b5b79" stroke="#fff" stroke-width="1.5"/>
    <circle cx="14" cy="32" r="9" fill="#8c8c8e" stroke="#fff" stroke-width="1.5"/>
    <path d="M52 16l8-4-3 8-1-3z" fill="#fff"/>
    <circle cx="74" cy="56" r="3.5" fill="none" stroke="#fff" stroke-width="1"/>
    <path d="M32 79c-3-4-4-6-4-8a4 4 0 0 1 8 0c0 2-1 4-4 8z" fill="none" stroke="#fff" stroke-width="1"/>
    <path d="M10 30h8l-4 6z" fill="none" stroke="#fff" stroke-width="1"/>
  </svg>
  <div class="abs" style="left:24px;top:47px;font-size:5.5px;color:var(--gold)">Lorem ipsum</div>
  <div class="cap abs" style="left:18px;top:56px;width:52px">Dolor sit amet, consectetur adipiscing elit, sed do eiusmod tempor</div>
  <div class="abs" style="left:24px;top:89px;font-size:5.5px;color:var(--grey)">Lorem ipsum</div>
  <div class="cap abs" style="left:18px;top:98px;width:52px">Dolor sit amet, consectetur adipiscing elit, sed do eiusmod tempor</div>
  <div class="abs" style="left:196px;top:47px;font-size:5.5px;color:var(--grey)">Lorem ipsum</div>
  <div class="cap abs" style="left:196px;top:56px;width:52px;text-align:left">Dolor sit amet, consectetur adipiscing elit, sed do eiusmod tempor</div>
  <div class="abs" style="left:196px;top:89px;font-size:5.5px;color:var(--teal)">Lorem ipsum</div>
  <div class="cap abs" style="left:196px;top:98px;width:52px;text-align:left">Dolor sit amet, consectetur adipiscing elit, sed do eiusmod tempor</div>
  <div class="footer-mark"></div><div class="footer-name">K7 Consulting &nbsp;|&nbsp; 1</div>
</section>

<!-- 12 Our chart: donuts -->
<section class="slide c3 r4">
  <div class="heading"><b>OUR</b> CHART</div>
  <svg class="abs" style="left:36px;top:46px" width="36" height="36" viewBox="0 0 36 36"><circle cx="18" cy="18" r="15" fill="none" stroke="#e2e6e9" stroke-width="4"/><circle cx="18" cy="18" r="15" fill="none" stroke="#1b5b79" stroke-width="4" stroke-dasharray="76.3 94.2" transform="rotate(-90 18 18)"/><text x="18" y="20" text-anchor="middle" font-size="6" font-weight="700" fill="#1b5b79" font-family="Roboto,sans-serif">81%</text></svg>
  <svg class="abs" style="left:114px;top:46px" width="36" height="36" viewBox="0 0 36 36"><circle cx="18" cy="18" r="15" fill="none" stroke="#e2e6e9" stroke-width="4"/><circle cx="18" cy="18" r="15" fill="none" stroke="#c9a867" stroke-width="4" stroke-dasharray="67.8 94.2" transform="rotate(-90 18 18)"/><text x="18" y="20" text-anchor="middle" font-size="6" font-weight="700" fill="#1b5b79" font-family="Roboto,sans-serif">72%</text></svg>
  <svg class="abs" style="left:190px;top:46px" width="36" height="36" viewBox="0 0 36 36"><circle cx="18" cy="18" r="15" fill="none" stroke="#e2e6e9" stroke-width="4"/><circle cx="18" cy="18" r="15" fill="none" stroke="#c9a867" stroke-width="4" stroke-dasharray="59.3 94.2" transform="rotate(-90 18 18)"/><text x="18" y="20" text-anchor="middle" font-size="6" font-weight="700" fill="#1b5b79" font-family="Roboto,sans-serif">63%</text></svg>
  <div class="cap abs" style="left:24px;top:88px;width:60px">dolor sit amet, consectetur adipiscing elit, sed do eiusmod tempor incididunt ut labore et dolore magna aliqua. Ut enim ad minim veniam, quis nostrud exercitation fugiat nulla pariatur.</div>
  <div class="cap abs" style="left:102px;top:88px;width:60px">dolor sit amet, consectetur adipiscing elit, sed do eiusmod tempor incididunt ut labore et dolore magna aliqua. Ut enim ad minim veniam, quis nostrud exercitation fugiat nulla pariatur.</div>
  <div class="cap abs" style="left:178px;top:88px;width:60px">dolor sit amet, consectetur adipiscing elit, sed do eiusmod tempor incididunt ut labore et dolore magna aliqua. Ut enim ad minim veniam, quis nostrud exercitation fugiat nulla pariatur.</div>
  <div class="footer-mark"></div><div class="footer-name">K7 Consulting &nbsp;|&nbsp; 1</div>
</section>

<!-- 13 Our chart: bars -->
<section class="slide c1 r5">
  <div class="heading"><b>OUR</b> CHART</div>
  <div class="abs" style="left:19px;top:45px;font-size:3.2px;font-weight:700;color:var(--teal)">Lorem ipsum dolor sit amet</div>
  <div class="body abs" style="left:19px;top:50px;width:124px">consectetur adipiscing elit, sed do eiusmod tempor incididunt ut labore et dolore magna aliqua. Ut enim ad minim veniam, quis nostrud exercitation ullamco laboris nisi ut aliquip ex ea commodo consequat. Duis aute irure dolor in reprehenderit in voluptate velit esse cillum dolore eu fugiat nulla pariatur.</div>
  <div class="abs" style="left:19px;top:86px;font-size:3.2px;font-weight:700;color:var(--teal)">Lorem ipsum dolor sit amet</div>
  <div class="body abs" style="left:19px;top:91px;width:124px">consectetur adipiscing elit, sed do eiusmod tempor incididunt ut labore et dolore magna aliqua. Ut enim ad minim veniam, quis nostrud exercitation ullamco laboris nisi ut aliquip ex ea commodo consequat. Duis aute irure dolor in reprehenderit in voluptate velit esse cillum dolore eu.</div>
  <svg class="abs" style="left:165px;top:28px" width="80" height="52" viewBox="0 0 80 52">
    <g stroke="#e5e5e5" stroke-width=".4"><path d="M4 6h74M4 16h74M4 26h74M4 36h74"/></g>
    <path d="M4 46h74" stroke="#999" stroke-width=".5"/>
    <rect x="6" y="16" width="3" height="30" fill="#1b5b79"/><rect x="10" y="28" width="3" height="18" fill="#bfbfbf"/><rect x="14" y="36" width="3" height="10" fill="#c9a867"/>
    <rect x="24" y="24" width="3" height="22" fill="#1b5b79"/><rect x="28" y="12" width="3" height="34" fill="#bfbfbf"/><rect x="32" y="30" width="3" height="16" fill="#c9a867"/>
    <rect x="42" y="18" width="3" height="28" fill="#1b5b79"/><rect x="46" y="22" width="3" height="24" fill="#bfbfbf"/><rect x="50" y="32" width="3" height="14" fill="#c9a867"/>
    <rect x="60" y="22" width="3" height="24" fill="#1b5b79"/><rect x="64" y="28" width="3" height="18" fill="#bfbfbf"/><rect x="68" y="12" width="3" height="34" fill="#c9a867"/>
    <g font-size="2.6" fill="#666" font-family="Roboto,sans-serif" text-anchor="middle"><text x="11" y="51">2009</text><text x="29" y="51">2010</text><text x="47" y="51">2011</text><text x="65" y="51">2012</text></g>
  </svg>
  <div class="abs" style="left:177px;top:84px;width:50px;font-size:2.5px;line-height:3.3px;color:#555"><span style="display:inline-block;width:3px;height:3px;background:var(--teal)"></span> <b>LOREM IPSUM</b><br>lorem ipsum dolor sit amet consectetur adipiscing sed do eiusmod<br><br><span style="display:inline-block;width:3px;height:3px;background:#bfbfbf"></span> <b>LOREM IPSUM</b><br>lorem ipsum dolor sit amet consectetur adipiscing sed do eiusmod<br><br><span style="display:inline-block;width:3px;height:3px;background:var(--gold)"></span> <b>LOREM IPSUM</b></div>
  <div class="footer-mark"></div><div class="footer-name">K7 Consulting &nbsp;|&nbsp; 1</div>
</section>

<!-- 14 Section title -->
<section class="slide c2 r5">
  <div class="photo" style="inset:0;background:linear-gradient(180deg,#2a6683 0%,#1f5d79 55%,#174f69 100%)" role="img" aria-label="Wind turbines over a field with teal overlay"></div>
  <div class="abs" style="left:118px;top:64px;width:30px;height:30px;border-radius:50%;background:var(--gold-soft);color:#fff;font-family:Georgia,serif;font-style:italic;font-weight:700;font-size:20px;display:flex;align-items:center;justify-content:center">i</div>
  <div class="abs" style="left:87px;top:98px;width:92px;height:.6px;background:rgba(255,255,255,.6)"></div>
  <div class="abs" style="left:0;width:266px;top:103px;text-align:center;font-family:'Roboto Condensed',sans-serif;font-size:8.5px;color:#fff">SECTION TITLE</div>
</section>

<!-- 15 Thank you -->
<section class="slide c3 r5">
  <div class="wordmark-box" style="left:18px;top:29.5px"></div>
  <div class="wordmark" style="left:31px;top:31.5px">K7 Consulting</div>
  <div class="photo" style="left:0;top:48px;width:266px;height:68px;background:linear-gradient(180deg,#2c6a88,#1c5a77 60%,#164e68)" role="img" aria-label="Solar panel array under sky with teal overlay"></div>
  <div class="abs" style="left:26px;top:69px;font-family:'Roboto Condensed',sans-serif;font-size:7px;color:#fff;border-bottom:1px solid var(--gold)">THANK YOU</div>
  <div class="abs" style="left:0;top:116px;width:266px;height:1px;background:var(--gold)"></div>
  <div class="abs" style="left:25px;top:128px;font-size:3px;color:#555"><span style="display:inline-block;width:5px;height:5px;border-radius:50%;border:.8px solid var(--gold);vertical-align:middle"></span> 2150 Harbor View Dr Ste 410</div>
  <div class="abs" style="left:114px;top:128px;font-size:3px;color:#555"><span style="display:inline-block;width:5px;height:5px;border-radius:50%;border:.8px solid var(--gold);vertical-align:middle"></span> support@kayseven.example</div>
  <div class="abs" style="left:196px;top:128px;font-size:3px;color:#555"><span style="display:inline-block;width:5px;height:5px;border-radius:50%;border:.8px solid var(--gold);vertical-align:middle"></span> www.kayseven.example</div>
  <div class="abs" style="left:0;bottom:0;width:266px;height:2px;background:var(--teal)"></div>
</section>

</main>
</body>
</html>
```